New webpage design for Varplen.se, participant management system informationpage.

Project Brief: New Website Design for Varplen.se (Participant Management System)
About Varplen.se:
Varplen.se is an established participant management system used by organizations and course providers in Sweden to handle event and course registrations. Our website’s primary audience is course providers, event organizers, and potential users seeking efficient management tools.
Project Goal:
We are launching a new public-facing website for Varplen.se, which will present information about our system, features, FAQ, pricing, news, testimonials, and more. The new site will be built in Umbraco CMS and should follow our visual identity as described in the attached graphic manual.
Deliverables:
We need complete, modern, and responsive page designs (desktop and mobile) for the following pages:
- Home page (landing page)
- Features page
- FAQ page
- About Us page
- Contact Us / Book a Demo page
- Pricing page
- Testimonials page
- News / Blog page
Design Guidelines:
- Please use the attached Lumoxa graphic manual for guidance (Lumoxa is a sister project; use the same branding).
- The Varplen.se logo is attached and must be included.
- Please use the blue color palette variant from the guide.
- Typography and graphic elements should be consistent with the manual.
- Designs must be suitable for implementation in Umbraco CMS (avoid overly complex layouts or animations that might be difficult to develop).
- All designs should be responsive and work well on desktop, tablet, and mobile.
- Final deliverables should be provided in Figma or Adobe XD (preferably Figma).
What We Like:
- Clean, modern, Scandinavian style.
- Clear navigation and strong hierarchy.
- Readable, accessible layouts.
What to Avoid:
- Overly playful or cartoonish elements.
- Too much clutter or excessive graphical elements.
- Dark color schemes (please focus on blue/light).
References:
- Our current site: https://varplen-example.se
- Graphic manual (see attachment)
- Varplen logo (see attachment)
Additional Notes:
- The new design should improve clarity, usability, and visual appeal compared to our current site.
- Feel free to suggest visual improvements, but remain consistent with our brand guidelines.
Other font styles liked:
- Orev and Cabin. See attached font files

```html
<!DOCTYPE html>
<html lang="en">
<head>
<meta charset="utf-8">
<title>Varplen – Participant management system</title>
<link href="https://fonts.googleapis.com/css2?family=Heebo:wght@300;400;500;700&display=swap" rel="stylesheet">
<style>
:root{
  --navy:#1f4e8c;
  --ink:#2b3a52;
  --muted:#7d8ba2;
  --label:#8fa3c2;
  --soft:#f2f4f8;
  --line:#e3e7ee;
  --white:#ffffff;
  --orange:#f0a04b;
}
*{box-sizing:border-box;margin:0;padding:0}
html,body{width:1200px;height:4040px;overflow:hidden}
body{font-family:"Heebo",Arial,sans-serif;color:var(--ink);background:var(--white);position:relative}
a{color:inherit;text-decoration:none}
.rainbow{height:3px;background:linear-gradient(90deg,#f2c14e,#e25a5a,#8e5ad8,#3b7be0,#3bbfa0,#f2c14e)}

.site-header{position:absolute;top:0;left:0;width:1200px;height:70px;background:var(--white)}
.site-header .rainbow{position:absolute;top:0;left:0;right:0;height:2px}
.brand{position:absolute;left:52px;top:14px;font-size:32px;font-weight:500;color:var(--ink);letter-spacing:.5px}
.main-nav a{position:absolute;top:27px;font-size:12px;letter-spacing:1.2px;color:#4a5670;text-transform:uppercase;white-space:nowrap}
.main-nav .caret{font-size:9px;margin-left:3px;color:var(--muted)}
.login{position:absolute;left:968px;top:25px;font-size:13px;color:var(--navy)}
.btn-contact{position:absolute;left:1041px;top:17px;width:110px;height:32px;border-radius:16px;background:var(--navy);color:var(--white);font-size:13px;font-weight:500;display:flex;align-items:center;justify-content:center}

.hero{position:absolute;top:70px;left:0;width:1200px;height:488px}

.section-label{font-size:15px;font-weight:300;color:var(--label)}
.section-title{font-size:30px;font-weight:300;color:var(--ink);margin-top:8px;line-height:38px}
.copy{font-size:13px;font-weight:300;color:var(--muted);line-height:20px}

.about{position:absolute;top:558px;left:0;width:1200px;height:466px}
.about .text{position:absolute;left:52px;top:34px;width:540px}
.about .paras{position:absolute;top:94px;left:0;width:530px}
.about .paras p{height:59px}
.btn{position:absolute;height:36px;border-radius:18px;display:flex;align-items:center;justify-content:center;font-size:13px}
.btn-primary{left:52px;top:381px;width:169px;background:var(--navy);color:var(--white);font-weight:500}
.btn-ghost{left:265px;top:381px;width:170px;border:1px solid #b9c4d6;color:var(--muted);font-weight:300}
.about-photo{position:absolute;left:707px;top:109px;width:441px;height:255px;border-radius:8px;background:linear-gradient(135deg,#c9ccc8 0%,#b8c6d6 45%,#8fb0d8 70%,#d9b45a 100%);box-shadow:0 14px 30px rgba(30,50,90,.22)}

.courses{position:absolute;top:1024px;left:0;width:1200px;height:783px;background:var(--soft)}
.courses .head{position:absolute;left:52px;top:36px}
.courses .intro{position:absolute;left:52px;top:140px;font-size:12px}
.course-card{position:absolute;color:var(--white);display:flex;flex-direction:column;justify-content:center;align-items:center;overflow:hidden}
.course-card .num{font-size:40px;font-weight:300;line-height:1}
.course-card .num small{font-size:12px;font-weight:300;opacity:.9}
.course-card .name{font-size:19px;font-weight:300;margin-top:10px;letter-spacing:.3px;white-space:nowrap}
.course-card.left{align-items:flex-start;padding-left:226px}
.c1{left:52px;top:229px;width:533px;height:281px;background:linear-gradient(135deg,#3d4a58,#5b6470 55%,#4a5360)}
.c2{left:613px;top:229px;width:535px;height:281px;background:linear-gradient(135deg,#7d8797,#9ba6b4 50%,#6d7a8c)}
.c3{left:52px;top:526px;width:346px;height:185px;background:linear-gradient(135deg,#3a4552,#6f7986)}
.c4{left:427px;top:526px;width:346px;height:185px;background:linear-gradient(135deg,#7f8b9a,#a7b1bd)}
.c5{left:802px;top:526px;width:346px;height:185px;background:linear-gradient(135deg,#6a727d,#8e959e)}
.c3 .num,.c4 .num,.c5 .num{font-size:36px}
.c3 .name,.c4 .name,.c5 .name{font-size:17px;margin-top:6px}

.features{position:absolute;top:1807px;left:0;width:1200px;height:692px;text-align:center}
.features .head{position:absolute;top:30px;left:0;width:1200px}
.features .intro{position:absolute;top:130px;left:0;width:1200px;font-size:12px}
.feature{position:absolute;width:270px;text-align:left}
.feature svg{display:block;width:44px;height:44px}
.feature h3{font-size:16px;font-weight:500;color:var(--ink);margin-top:30px;letter-spacing:.3px}
.feature .copy{font-size:12px;line-height:20px;margin-top:14px}

.people{position:absolute;top:2499px;left:0;width:1200px;height:411px;background:var(--soft)}
.people .head{position:absolute;left:52px;top:40px}
.people .intro{position:absolute;left:52px;top:140px;font-size:12px}
.quote{position:absolute;top:215px;width:357px;height:135px;background:var(--white);border-radius:3px;padding:26px 10px 0 101px}
.quote .avatar{position:absolute;left:23px;top:27px;width:50px;height:50px;border-radius:50%;background:radial-gradient(circle at 50% 40%,#a88a78,#4a3a34)}
.quote p{font-size:12px;font-style:italic;font-weight:300;color:var(--label);line-height:20px}
.quote .who{font-size:12px;color:#4a5670;margin-top:10px;font-weight:300}

.blog{position:absolute;top:2910px;left:0;width:1200px;height:609px}
.blog .head{position:absolute;left:52px;top:22px}
.blog .intro{position:absolute;left:52px;top:126px;font-size:12px}
.post{position:absolute;top:196px;width:252px;background:var(--white);box-shadow:0 2px 10px rgba(30,50,90,.08);border-radius:3px}
.post .thumb{height:190px;border-radius:3px 3px 0 0}
.post .body{padding:12px 19px 16px}
.post h4{font-size:17px;font-weight:400;color:#4a5670;white-space:nowrap}
.post .copy{font-size:11px;line-height:19px;margin-top:8px}
.post .meta{border-top:1px solid var(--line);margin-top:12px;padding-top:12px;display:flex;justify-content:space-between;font-size:10px;color:var(--muted);font-weight:300}

.partners{position:absolute;top:3519px;left:0;width:1200px;height:365px;background:var(--soft);text-align:center}
.partners .head{position:absolute;top:38px;left:0;width:1200px}
.partner{position:absolute;top:218px;width:120px;margin-left:-60px;display:flex;flex-direction:column;align-items:center}
.partner .mark{height:50px;display:flex;align-items:center;justify-content:center}
.partner .tag{font-size:12px;letter-spacing:1.2px;color:var(--muted);margin-top:8px;font-weight:300}

.site-footer{position:absolute;top:3884px;left:0;width:1200px;height:156px;background:var(--white)}
.site-footer .rainbow{height:2px}
.foot-main{position:absolute;top:42px;left:52px;right:52px;display:flex;align-items:center;font-size:13px;color:#3c4a63}
.foot-main a{margin-right:26px}
.foot-main .search{margin-right:22px;display:flex}
.foot-main .flag{margin-left:auto;width:22px;height:14px;background:linear-gradient(180deg,#c9475a 0 50%,#eef0f4 50%);position:relative}
.foot-main .flag::before{content:"";position:absolute;left:0;top:0;width:9px;height:8px;background:#3a5aa8}
.foot-divider{position:absolute;top:74px;left:52px;right:52px;height:1px;background:var(--line)}
.foot-sub{position:absolute;top:86px;left:52px;right:52px;display:flex;font-size:11px;color:var(--muted);font-weight:300;letter-spacing:.4px}
.foot-sub a{margin-right:20px}
.foot-sub .legal{margin-left:auto;display:flex;gap:20px}
</style>
</head>
<body>

<header class="site-header">
  <div class="rainbow"></div>
  <a class="brand" href="#">varplen.</a>
  <nav class="main-nav">
    <a href="#" style="left:367px">About us</a>
    <a href="#" style="left:470px">Our system<span class="caret">⌵</span></a>
    <a href="#" style="left:605px">Price</a>
    <a href="#" style="left:679px">Features<span class="caret">⌵</span></a>
    <a href="#" style="left:794px">Blog</a>
  </nav>
  <a class="login" href="#">Log In</a>
  <a class="btn-contact" href="#">Book a demo</a>
</header>

<section class="hero">
  <svg width="1200" height="488" viewBox="0 0 1200 488">
    <defs>
      <linearGradient id="heroA" x1="0" y1="0" x2="1" y2="1"><stop offset="0" stop-color="#d7dbde"/><stop offset=".5" stop-color="#a99283"/><stop offset="1" stop-color="#6f7a88"/></linearGradient>
      <linearGradient id="heroB" x1="0" y1="0" x2="1" y2="1"><stop offset="0" stop-color="#6b4a33"/><stop offset=".5" stop-color="#a07a5a"/><stop offset="1" stop-color="#4b3526"/></linearGradient>
      <linearGradient id="heroC" x1="0" y1="0" x2="1" y2="1"><stop offset="0" stop-color="#e9ecef"/><stop offset=".55" stop-color="#b9c2cc"/><stop offset="1" stop-color="#3f4d60"/></linearGradient>
    </defs>
    <rect width="1200" height="488" fill="#ffffff"/>
    <polygon role="img" aria-label="Photo: course organisers planning registrations at a laptop" points="0,0 549,0 290,488 0,488" fill="url(#heroA)"/>
    <polygon role="img" aria-label="Photo: handshake over a desk with laptop and documents" points="567,0 957,0 729,488 308,488" fill="url(#heroB)"/>
    <polygon role="img" aria-label="Photo: presenter speaking to course participants" points="975,0 1200,0 1200,488 747,488" fill="url(#heroC)"/>
  </svg>
</section>

<section class="about">
  <div class="text">
    <div class="section-label">About us</div>
    <h2 class="section-title">Who we are</h2>
    <div class="paras copy">
      <p>Varplen is a participant management system that helps Swedish course providers and event organisers handle registrations with ease.</p>
      <p>Create event pages, open online sign-up and keep every participant list up to date in one place, without spreadsheets or manual work.</p>
      <p>Invoices, confirmations and reminders are sent automatically, so you can spend your time on the course content and your participants.</p>
      <p>Thousands of organisations trust Varplen every year, from small training firms to large associations running hundreds of events.</p>
    </div>
  </div>
  <a class="btn btn-primary" href="#">Read more</a>
  <a class="btn btn-ghost" href="#">Our system</a>
  <div class="about-photo" role="img" aria-label="Photo: course organiser working on a tablet with a stylus"></div>
</section>

<section class="courses">
  <div class="head">
    <div class="section-label">System</div>
    <h2 class="section-title">Our System</h2>
  </div>
  <p class="intro copy">Everything you need to run courses and events<br>From the first registration to the final invoice, all in one clear tool</p>

  <a class="course-card c1" href="#" role="img" aria-label="Photo: modern meeting room ready for a course">
    <div class="num">5<small> / Tools</small></div>
    <div class="name">Online registration</div>
  </a>
  <a class="course-card c2 left" href="#" role="img" aria-label="Photo: person writing notes at a desk">
    <div class="num">4<small> / Tools</small></div>
    <div class="name">Invoicing</div>
  </a>
  <a class="course-card c3" href="#" role="img" aria-label="Photo: open-plan office with people at desks">
    <div class="num">6<small> / Tools</small></div>
    <div class="name">Participant lists</div>
  </a>
  <a class="course-card c4" href="#" role="img" aria-label="Photo: hands working with papers and a laptop">
    <div class="num">3<small> / Tools</small></div>
    <div class="name">Event pages</div>
  </a>
  <a class="course-card c5" href="#" role="img" aria-label="Photo: team reviewing reports at a table">
    <div class="num">4<small> / Tools</small></div>
    <div class="name">Reports &amp; statistics</div>
  </a>
</section>

<section class="features">
  <div class="head">
    <div class="section-label">Features</div>
    <h2 class="section-title">Why choose varplen</h2>
  </div>
  <p class="intro copy">A simple and secure way to manage<br>registrations, participants and payments for every event</p>

  <div class="feature" style="left:193px;top:245px">
    <svg viewBox="0 0 44 44"><path d="M8 2h19l10 10v30H8z" fill="var(--navy)"/><path d="M27 2v10h10" fill="#8fa9cf"/><rect x="14" y="22" width="17" height="2.4" fill="#fff"/><rect x="14" y="28" width="17" height="2.4" fill="#fff"/><rect x="14" y="34" width="17" height="2.4" fill="#fff"/></svg>
    <h3>Easy registration forms</h3>
    <p class="copy">Build custom sign-up forms in minutes<br>and publish them on your own website</p>
  </div>
  <div class="feature" style="left:475px;top:245px">
    <svg viewBox="0 0 44 44"><g fill="var(--navy)"><rect x="0" y="5" width="10" height="9" rx="1.5"/><rect x="13" y="5" width="31" height="9" rx="1.5"/><rect x="0" y="17" width="10" height="9" rx="1.5"/><rect x="13" y="17" width="31" height="9" rx="1.5"/><rect x="0" y="29" width="10" height="9" rx="1.5"/><rect x="13" y="29" width="31" height="9" rx="1.5"/></g></svg>
    <h3>Participant lists</h3>
    <p class="copy">See every participant, waiting list and<br>attendance status in one clear overview</p>
  </div>
  <div class="feature" style="left:756px;top:245px">
    <svg viewBox="0 0 44 44"><g fill="var(--navy)"><rect x="2" y="9" width="38" height="3"/><rect x="2" y="21" width="38" height="3"/><rect x="2" y="33" width="38" height="3"/><rect x="25" y="5" width="7" height="11" rx="1"/><rect x="9" y="17" width="7" height="11" rx="1"/><rect x="19" y="29" width="7" height="11" rx="1"/></g></svg>
    <h3>Flexible settings</h3>
    <p class="copy">Set prices, discounts and seat limits<br>exactly the way your events need</p>
  </div>
  <div class="feature" style="left:193px;top:470px">
    <svg viewBox="0 0 44 44"><path d="M22 3l5.6 12.3 13.4 1.4-10 9 2.9 13.2L22 32.1 10.1 38.9 13 25.7 3 16.7l13.4-1.4z" fill="var(--navy)"/></svg>
    <h3>Trusted support</h3>
    <p class="copy">Friendly Swedish support team ready<br>to help you on weekdays</p>
  </div>
  <div class="feature" style="left:475px;top:470px">
    <svg viewBox="0 0 48 44"><g fill="var(--navy)"><path d="M24 1L1 11v3h46v-3z"/><rect x="3" y="16" width="42" height="3"/><rect x="6" y="20" width="4" height="16"/><rect x="14" y="20" width="4" height="16"/><rect x="22" y="20" width="4" height="16"/><rect x="30" y="20" width="4" height="16"/><rect x="38" y="20" width="4" height="16"/><rect x="3" y="37" width="42" height="3"/><rect x="0" y="41" width="48" height="3"/></g></svg>
    <h3>Automated invoicing</h3>
    <p class="copy">Invoices and receipts are created and<br>sent as soon as people register</p>
  </div>
  <div class="feature" style="left:756px;top:470px">
    <svg viewBox="0 0 44 44"><circle cx="18" cy="18" r="12.5" fill="none" stroke="var(--navy)" stroke-width="5"/><path d="M27 27l12 12" stroke="var(--navy)" stroke-width="6" stroke-linecap="round"/></svg>
    <h3>Smart search</h3>
    <p class="copy">Find any participant, booking or<br>payment in just a few seconds</p>
  </div>
</section>

<section class="people">
  <div class="head">
    <div class="section-label">Testimonials</div>
    <h2 class="section-title">What do people say for us?</h2>
  </div>
  <p class="intro copy">Course providers and organisers share their experience</p>

  <article class="quote" style="left:56px">
    <div class="avatar" role="img" aria-label="Portrait photo of Anna Lindqvist"></div>
    <p>Registrations that took us days now<br>take minutes. Our participants love<br>how simple it is to sign up.</p>
    <div class="who">Anna Lindqvist , Course coordinator</div>
  </article>
  <article class="quote" style="left:422px">
    <div class="avatar" role="img" aria-label="Portrait photo of Sara Holmberg" style="background:radial-gradient(circle at 50% 40%,#c9a89a,#5a3e3a)"></div>
    <p>Automatic invoices have saved our<br>office many hours every month,<br>and the support is excellent.</p>
    <div class="who">Sara Holmberg , Event manager</div>
  </article>
  <article class="quote" style="left:787px">
    <div class="avatar" role="img" aria-label="Portrait photo of Johan Ekdahl" style="background:radial-gradient(circle at 50% 40%,#b39480,#3e3430)"></div>
    <p>We run over a hundred events a year<br>and always know who is coming.<br>A clear and reliable system.</p>
    <div class="who">Johan Ekdahl , Training director</div>
  </article>
</section>

<section class="blog">
  <div class="head">
    <div class="section-label">News</div>
    <h2 class="section-title">Latest blog post</h2>
  </div>
  <p class="intro copy">News, product updates and practical tips for course providers and event organisers using Varplen every day.</p>

  <article class="post" style="left:52px">
    <div class="thumb" role="img" aria-label="Article image: new registration form editor on a laptop" style="background:linear-gradient(135deg,#1d4a86,#2b5c9c 60%,#c98a5a)"></div>
    <div class="body">
      <h4>New form editor...</h4>
      <p class="copy">Our redesigned form editor makes it easier than ever to build custom sign-up...</p>
      <div class="meta"><span>▦ 12 Aug, 2025</span><span>● 0</span></div>
    </div>
  </article>
  <article class="post" style="left:333px">
    <div class="thumb" role="img" aria-label="Article image: charts and documents on a desk" style="background:linear-gradient(180deg,#3e78c2 0%,#bcd0e8 35%,#ffffff 36%,#f4f6fa 100%)"></div>
    <div class="body">
      <h4>5 tips for more sig...</h4>
      <p class="copy">Simple ways to fill every seat at your next course and reduce no-shows...</p>
      <div class="meta"><span>▦ 05 Aug, 2025</span><span>● 0</span></div>
    </div>
  </article>
  <article class="post" style="left:612px">
    <div class="thumb" role="img" aria-label="Article image: invoice overview on a calculator" style="background:linear-gradient(180deg,#5b6a80 0%,#1f4e8c 40%,#1f4e8c 58%,#4a5568 100%)"></div>
    <div class="body">
      <h4>Faster invoicing...</h4>
      <p class="copy">Invoices are now sent directly after each registration...</p>
      <div class="meta"><span>▦ 30 Jul, 2025</span><span>● 0</span></div>
    </div>
  </article>
  <article class="post" style="left:891px">
    <div class="thumb" role="img" aria-label="Article image: two people shaking hands at a partnership meeting" style="background:linear-gradient(180deg,#eef0f3 0%,#dfe3ea 40%,#2f4f86 75%,#1d3564 100%)"></div>
    <div class="body">
      <h4>New integration p...</h4>
      <p class="copy">Varplen now connects with more accounting tools...</p>
      <div class="meta"><span>▦ 28 Jul, 2025</span><span>● 0</span></div>
    </div>
  </article>
</section>

<section class="partners">
  <div class="head">
    <div class="section-label">Partners</div>
    <h2 class="section-title">Who are the partners and<br>our collaborators { varplen }</h2>
  </div>
  <div class="partner" style="left:187px"><div class="mark"><svg width="60" height="40"><rect width="60" height="40" fill="#1c3f6e"/></svg></div><div class="tag">PARTNER</div></div>
  <div class="partner" style="left:322px"><div class="mark"><svg width="56" height="34"><rect width="56" height="34" rx="4" fill="#3aa548"/></svg></div><div class="tag">CUSTOMER</div></div>
  <div class="partner" style="left:460px"><div class="mark"><svg width="72" height="40"><rect width="72" height="40" rx="3" fill="#d9443a"/></svg></div><div class="tag">PARTNER</div></div>
  <div class="partner" style="left:595px;top:210px"><div class="mark" style="height:70px"><svg width="86" height="70"><circle cx="43" cy="35" r="34" fill="#2a3f9c"/></svg></div></div>
  <div class="partner" style="left:731px"><div class="mark"><svg width="50" height="50"><circle cx="25" cy="25" r="22" fill="#5b6fd6"/></svg></div><div class="tag">CUSTOMER</div></div>
  <div class="partner" style="left:867px"><div class="mark"><svg width="46" height="46"><rect x="3" y="3" width="40" height="40" rx="10" fill="#4a7fe0"/></svg></div><div class="tag">PARTNER</div></div>
  <div class="partner" style="left:1002px"><div class="mark"><svg width="50" height="50"><circle cx="25" cy="25" r="22" fill="var(--orange)"/><path d="M25 15v20M15 25h20" stroke="#fff" stroke-width="3" stroke-linecap="round"/></svg></div><div class="tag">SEE MORE</div></div>
</section>

<footer class="site-footer">
  <div class="rainbow"></div>
  <div class="foot-main">
    <span class="search"><svg width="14" height="14" viewBox="0 0 14 14"><circle cx="6" cy="6" r="4.2" fill="none" stroke="var(--navy)" stroke-width="2"/><path d="M9 9l4 4" stroke="var(--navy)" stroke-width="2" stroke-linecap="round"/></svg></span>
    <a href="#">Help &amp; Contact</a>
    <a href="#">Features</a>
    <a href="#">Pricing</a>
    <a href="#">Blog</a>
    <span class="flag" role="img" aria-label="Language selector"></span>
  </div>
  <div class="foot-divider"></div>
  <div class="foot-sub">
    <a href="#">About us</a>
    <a href="#">Careers</a>
    <a href="#">FAQ</a>
    <a href="#">Testimonials</a>
    <a href="#">Partners</a>
    <a href="#">Book a demo</a>
    <div class="legal"><span>© 2020 - 2025</span><a href="#">Privacy</a><a href="#">Terms</a></div>
  </div>
</footer>

</body>
</html>
```